Web Design Project

I need designs (PSD only - no programming) for several pages of a new website helping train operators to manage key information about their traindrivers.
The main feature of this website is the management of personnel records (create, edit, search, delete). Another key aspect is the management of user privileges. Since this is a new website we also need a user friendly frontpage, pricing information and how it works sections.
This can be broken down into 9 pages for which we need designs (PSDs).
1. Home
2. Driver record
3. How it works
4. Pricing
5. User administration
6. Help
7. Record list view
8. Login
9. Registration
Navigation (not logged in) are: Home | How it works | Pricing | Customers | About us | Contact
Navigation (logged in) are: Overview | Administration | Manage records | Billing | Help | Contact
Footer: Customer logos | Awards | Terms & Conditions | Privacy
To provide the best support for you to come up with a strong design proposal I will provide DAILY feedback to all participants. We have also created concept mockups (attached) and example pages (below) for each section to give you a clear sense of what we look for.
The core concepts for a successful bid are that the website is EASY to understand, INTUITIVE to navigate, and SIMPLE to use. Most of our users lack technical background and are looking for tool to simplify their work.
The strongest participants (winner and close contenders) will have the opportunity to additional commissioned work on additional sections not included in this brief.
Example Pages (by section)
1. http://www.brovendale.example/site-keepers/
1. http://www.qvt.example/
1. http://www.mondaph.example/
1. http://www.gorvanquest.example/
2. http://www.snapveld.example/profile_edit.gne
3. https://www.tarn.example/how-it-works/
3. http://www.bulkvue.example/learn
4. http://www.pactheron.example/crm/editions-pricing.jsp
4. http://www.brovendale.example/site-keepers/prices
6. https://support.talvora.example/en-gb/
6. http://help.dealmeadow.example/contact_us
8. https://www.careweave.example/uas/login
8. https://www.dealmeadow.example/login
8. http://www.askhollow.example/login/index
For form designs we like Verindo, Bidnook, Snapveld, CareWeave, Chatterly and the concepts presented by Tomas Kerrigan in his classic Layout Craft Shaping the Input Boxes.
For additional guidance see mockups attached!
Target Market(s)
Security, human resources and admin support employees for train operators.
Industry/Entity Type
Learn
Requirements
Should not have
- Home page should not have
Social media icons (chatterly, chirpla, CareWeave, RSS feed)
Contact forms
Read more links
Old trains

```html
<!DOCTYPE html>
<html lang="en">
<head>
<meta charset="utf-8">
<title>RailRoster — Home</title>
<link rel="stylesheet" href="https://fonts.googleapis.com/css2?family=Arimo:wght@400;700&display=swap">
<style>
:root{
  --red:#d10f14;
  --red-dark:#8a1627;
  --grey-text:#7a7a7a;
  --icon:#6f6f6f;
  --band:#e6e2df;
  --lilac:#e3e4ec;
  --logo:#7e93c3;
  --white:#ffffff;
}
*{margin:0;padding:0;box-sizing:border-box}
html,body{width:974px;height:1200px;overflow:hidden}
body{font-family:"Arimo",Arial,sans-serif;background:#e8e6e3}
.stage{position:absolute;left:0;top:0;width:1200px;height:1479px;transform:scale(.81166);transform-origin:0 0;
  background:linear-gradient(180deg,#d9d3cd 0%,#f4f2ef 25%,#ffffff 40%,#ece9e6 60%,#dcd9d7 100%)}
.page{position:absolute;left:257px;top:0;width:686px;height:1479px;box-shadow:0 0 12px rgba(0,0,0,.35);
  background:linear-gradient(180deg,#d8d2cb 0,#e7e1da 85px)}
.abs{position:absolute}
/* header */
.util{top:13px;font-size:10px;color:#fff;letter-spacing:.2px}
.util span{position:absolute;white-space:nowrap}
.util .lang u{color:#fff}
.search{left:543px;top:11px;width:108px;height:18px;background:var(--red-dark);color:#fff;font-size:10px;padding:3px 8px}
.search svg{position:absolute;right:5px;top:3px}
.brand{left:17px;top:44px;font-size:27px;font-weight:700;color:var(--logo);letter-spacing:-.5px}
.nav{top:60px;font-size:10.5px;color:var(--red-dark)}
.nav a{position:absolute;white-space:nowrap;text-decoration:none;color:inherit}
.nav-mark{left:259px;top:80px;width:0;height:0;border-left:6px solid transparent;border-right:6px solid transparent;border-bottom:6px solid var(--red)}
/* hero */
.hero{left:0;top:85px;width:686px;height:170px;
  background:
    radial-gradient(ellipse 70px 120px at 450px 95px,rgba(70,10,10,.75),rgba(70,10,10,0)),
    linear-gradient(180deg,rgba(255,90,90,0) 0%,rgba(255,120,120,.35) 22%,rgba(255,90,90,0) 32%,rgba(90,0,0,0) 60%,rgba(90,0,0,.45) 100%),
    linear-gradient(90deg,#a50d10 0%,#e01515 18%,#f02222 32%,#c81212 46%,#9e0d0f 60%,#d41414 72%,#a30e10 86%,#e21a1a 100%)}
.hero-title{left:250px;top:220px;font-size:28px;font-weight:700;color:#fff;letter-spacing:-.8px;white-space:nowrap}
.hero-more{left:568px;top:233px;font-size:10px;color:#fff;font-style:italic;white-space:nowrap}
/* signup */
.signup{left:0;width:686px;height:39px;background:var(--band)}
.signup .field{position:absolute;left:110px;top:9px;width:159px;height:21px;background:var(--red);color:#fff;font-size:12px;font-style:italic;padding:3px 9px;white-space:nowrap}
.signup .btn{position:absolute;left:269px;top:9px;width:107px;height:21px;background:linear-gradient(180deg,#e07176,#c5383e);color:#fff;font-size:12.5px;font-weight:700;padding:3px 12px;white-space:nowrap}
.signup .call{position:absolute;left:394px;top:12px;font-size:12.5px;font-weight:700;color:var(--red);white-space:nowrap}
/* benefits */
.benefits{left:0;top:294px;width:686px;height:324px;background:linear-gradient(160deg,#f0ebe6 0%,#e6dbcf 45%,#f4efe8 75%,#faf7f3 100%)}
.benefit h3{font-size:12.5px;font-weight:700;color:var(--red)}
.benefit p{font-size:12px;line-height:13px;color:var(--grey-text)}
.five{left:87px;top:490px;font-size:100px;color:var(--red);line-height:1}
.five-label{left:147px;top:548px;font-size:33px;font-weight:700;color:var(--red)}
.photo{background:linear-gradient(180deg,#b9b8b6,#6f7180)}
/* how it works */
.how{left:0;top:657px;width:686px;height:300px;background:var(--lilac)}
.section-title{font-size:33px;font-weight:700;color:var(--red)}
.step h3{font-size:12.5px;font-weight:700;color:var(--red)}
.step ol{margin-top:6px;font-size:12px;line-height:16px;color:var(--grey-text);padding-left:18px}
.badge{width:30px;height:28px;background:var(--icon);color:#fff;font-weight:700;font-size:17px;text-align:center;padding-top:5px}
/* customers */
.customers{left:0;top:957px;width:686px;height:522px;background:linear-gradient(180deg,#d8d9e2 0%,#e3e3ea 30%,#d5d6df 60%,#b9bcc8 100%)}
.footer-links{font-size:10.5px;color:var(--red);line-height:16px}
.footer-links a{display:block;color:inherit;text-decoration:none}
.streak{left:180px;top:1265px;width:506px;height:90px;background:linear-gradient(180deg,#c8d4e6,#f2f4f8 60%,#a9b0c1)}
.legal-band{left:176px;top:1345px;width:510px;height:63px;background:linear-gradient(90deg,rgba(138,22,39,.2),var(--red-dark) 30%)}
.legal{left:464px;top:1357px;font-size:10px;line-height:16px;color:#fff}
</style>
</head>
<body>
<div class="stage">
  <div class="page">
    <div class="abs util">
      <span style="left:286px">Signup</span><span style="left:328px">|</span>
      <span style="left:350px">Login</span><span style="left:385px">|</span>
      <span class="lang" style="left:408px">Language : <u>English</u> ▾</span><span style="left:522px">|</span>
    </div>
    <div class="abs search">Type to search
      <svg width="11" height="11" viewBox="0 0 11 11"><circle cx="4.5" cy="4.5" r="3.5" fill="none" stroke="#fff" stroke-width="1.3"/><line x1="7" y1="7" x2="10" y2="10" stroke="#fff" stroke-width="1.3"/></svg>
    </div>
    <div class="abs brand">RAILROSTER</div>
    <nav class="abs nav">
      <a style="left:250px">HOME</a><a style="left:294px">HOW IT WORKS</a><a style="left:384px">PRICES</a>
      <a style="left:434px">OUR CUSTOMERS</a><a style="left:538px">ABOUT US</a><a style="left:603px">CONTACT</a>
    </nav>

    <div class="abs hero" role="img" aria-label="Red-toned motion-blurred photo of a station platform with a traveller walking past a train"></div>
    <div class="abs nav-mark"></div>
    <div class="abs hero-title">WHY RAIL ROSTER?</div>
    <div class="abs hero-more"><u>View More</u> »</div>

    <div class="abs signup" style="top:255px"><div class="field">Enter your e-mail address</div><div class="btn">SIGNUP NOW</div><div class="call">OR CALL NOW! 1-800-402915</div></div>

    <section class="abs benefits"></section>
    <svg class="abs" style="left:26px;top:318px" width="52" height="50" viewBox="0 0 52 50"><text x="0" y="38" font-family="Arimo,Arial,sans-serif" font-weight="700" font-size="36" fill="#6f6f6f" letter-spacing="-4">123</text></svg>
    <div class="abs benefit" style="left:109px;top:323px;width:200px"><h3>EASY TO USE</h3><p>Help text, reminders of important dates and events</p></div>
    <svg class="abs" style="left:28px;top:393px" width="46" height="56" viewBox="0 0 46 56"><path d="M4 8 L20 2 L44 6 V48 L20 54 L4 48Z" fill="#6f6f6f"/><rect x="10" y="18" width="12" height="14" rx="2" fill="none" stroke="#e8e0d8" stroke-width="2"/></svg>
    <div class="abs benefit" style="left:109px;top:399px"><h3>SAFE</h3><p>Securely stored in the cloud</p></div>
    <svg class="abs" style="left:342px;top:326px" width="56" height="58" viewBox="0 0 56 58"><path d="M14 34 a10 10 0 0 1 2-20 a14 14 0 0 1 26 2 a9 9 0 0 1 0 18" fill="none" stroke="#6f6f6f" stroke-width="2.5"/><path d="M24 48 V24 a3 3 0 0 1 6 0 V36 l6 1 a4 4 0 0 1 3 4 V50 a6 6 0 0 1 -6 6 H28 a6 6 0 0 1 -5-3 l-5-8 a2.5 2.5 0 0 1 4-3 Z" fill="none" stroke="#6f6f6f" stroke-width="2.5" stroke-linejoin="round"/></svg>
    <div class="abs benefit" style="left:428px;top:323px;width:190px"><h3>ACCESSIBLE</h3><p>Storage allow easy access from anywhere and privilege rights accross different users, allow collaboratives work</p></div>
    <svg class="abs" style="left:354px;top:413px" width="44" height="60" viewBox="0 0 44 60" role="img" aria-label="Running figure icon">
      <circle cx="12" cy="8" r="6" fill="#6f6f6f"/>
      <path d="M14 17 L22 30 L34 34" fill="none" stroke="#6f6f6f" stroke-width="7" stroke-linecap="round" stroke-linejoin="round"/>
      <path d="M14 17 L4 24" fill="none" stroke="#6f6f6f" stroke-width="5" stroke-linecap="round"/>
      <path d="M22 30 L14 42 L18 56" fill="none" stroke="#6f6f6f" stroke-width="7" stroke-linecap="round" stroke-linejoin="round"/>
      <path d="M22 34 L30 46 L41 46" fill="none" stroke="#6f6f6f" stroke-width="7" stroke-linecap="round" stroke-linejoin="round"/>
    </svg>
    <div class="abs benefit" style="left:428px;top:413px;width:200px"><h3>FAST</h3><p>Pre-filled fields, logical structure, smart categories, one-click PDF generation</p></div>
    <svg class="abs" style="left:359px;top:506px" width="36" height="46" viewBox="0 0 36 46"><rect x="2" y="2" width="32" height="42" fill="#6f6f6f"/><rect x="6" y="2" width="4" height="12" fill="#e8e0d8"/></svg>
    <div class="abs benefit" style="left:428px;top:515px"><h3>EU Compliant</h3><p>Follows the latest directives</p></div>
    <div class="abs photo" style="left:6px;top:465px;width:68px;height:153px;background:linear-gradient(180deg,#d8d8d6,#9c9ea6 55%,#3e4058)" role="img" aria-label="Photo of a uniformed train driver holding a cap"></div>
    <div class="abs five">5</div>
    <div class="abs five-label">BENEFITS</div>

    <div class="abs signup" style="top:618px;background:#f3efe9"><div class="field">Enter your e-mail address</div><div class="btn">SIGNUP NOW</div><div class="call">OR CALL NOW! 1-800-402915</div></div>

    <section class="abs how"></section>
    <h2 class="abs section-title" style="left:25px;top:679px">How it works?</h2>
    <div class="abs badge" style="left:29px;top:747px">A</div>
    <svg class="abs" style="left:70px;top:751px" width="50" height="60" viewBox="0 0 50 60" role="img" aria-label="Icon of a driver filing a record">
      <rect x="20" y="2" width="14" height="5" fill="#6f6f6f"/>
      <rect x="18" y="7" width="18" height="3" fill="#6f6f6f"/>
      <circle cx="27" cy="15" r="5" fill="#6f6f6f"/>
      <path d="M22 22 H40 a8 8 0 0 1 8 8 V58 H22 Z" fill="#6f6f6f"/>
      <path d="M24 30 L12 36" stroke="#6f6f6f" stroke-width="5" stroke-linecap="round"/>
      <rect x="2" y="32" width="20" height="26" fill="none" stroke="#6f6f6f" stroke-width="3"/>
      <line x1="2" y1="45" x2="22" y2="45" stroke="#6f6f6f" stroke-width="2"/>
    </svg>
    <div class="abs step" style="left:141px;top:746px"><h3>REGISTER A DRIVER</h3><ol><li>Click 'new certificate'</li><li>Register driver information</li><li>Click 'save'</li></ol></div>
    <div class="abs badge" style="left:361px;top:747px">C</div>
    <svg class="abs" style="left:411px;top:752px" width="54" height="46" viewBox="0 0 54 46"><rect x="2" y="4" width="38" height="28" fill="none" stroke="#6f6f6f" stroke-width="3"/><circle cx="40" cy="20" r="8" fill="#6f6f6f"/><path d="M35 26 L33 42 L40 36 L47 42 L45 26" fill="#6f6f6f"/></svg>
    <div class="abs step" style="left:480px;top:746px"><h3>GENERATE A CERTIFICATE</h3><ol><li>Search record</li><li>Click 'print PDF'</li></ol></div>
    <div class="abs badge" style="left:29px;top:857px">B</div>
    <svg class="abs" style="left:78px;top:856px" width="42" height="56" viewBox="0 0 42 56"><rect x="2" y="2" width="38" height="52" fill="none" stroke="#6f6f6f" stroke-width="3"/><line x1="2" y1="28" x2="40" y2="28" stroke="#6f6f6f" stroke-width="3"/><path d="M16 8 v5 h10 v-5 M16 34 v5 h10 v-5" fill="none" stroke="#6f6f6f" stroke-width="2"/></svg>
    <div class="abs step" style="left:143px;top:851px"><h3>REGISTER AN UPDATE</h3><ol><li>Search record</li><li>Update field(s)</li><li>Click 'save'</li></ol></div>

    <section class="abs customers"></section>
    <h2 class="abs section-title" style="left:24px;top:980px;font-size:25px">Our Customers</h2>
    <div class="abs streak"></div>
    <div class="abs legal-band"></div>
    <div class="abs footer-links" style="left:464px;top:1190px"><a>HOME</a><a>HOW IT WORKS</a><a>PRICES</a><a>OUR CUSTOMERS</a></div>
    <div class="abs footer-links" style="left:588px;top:1190px"><a>ABOUT US</a><a>CONTACT</a></div>
    <div class="abs legal">COPYRIGHT © 2012 RailRoster<br>All rights reserved<br>T&amp;C</div>
    <div class="abs photo" style="left:0;top:1222px;width:262px;height:257px;background:radial-gradient(ellipse 110px 150px at 110px 200px,#3a3a42,rgba(58,58,66,.6) 60%,rgba(200,200,210,0) 100%)" role="img" aria-label="Photo of a businessman in glasses talking on a phone"></div>
  </div>
</div>
</body>
</html>
```